Harbor Lantern Guidance Graphics

We need help to design a logo, graphics, layout that will represent a particular type of leadership consulting business that we are about to launch. The design/graphics should be able to be used for developing a brochure, web page, advertisements, letterhead, business cards, etc. The leadership consulting business that we are launching is called “Harbor Lantern Guidance.” We would like to start with the design of a brochure. We have enclosed a draft to give you some ideas about the type of graphics we are looking for. The graphics should include fonts, colors, pictures/symbols, and layout initially for the brochure only. There are three draft pictures/symbols that we have gotten from the internet for the attached brochure that may be copyrighted. We would like you to develop something similar, but original for each of the graphic’s. They each represent a theme/topic that we will be using. For example, the graphic for the section titled “What is Harbor Lantern Guidance?” has a picture/graphic that has a diverse group of people to represent the idea of Collective Leadership. It leaves out some of the facial features for each person in order to make sure that there are no similarities to real persons. We need something similar to this. The graphic for “Why is Harbor Lantern Guidance important?”, uses a picture of “ice” and a “mouse.” “Owls and Sand” is a key metaphor that we will use in our business. We need something to represent this concept. The same is true for the third picture that represents ripples in water. After design of the brochure we may seek additional help for the web page and other items.

Target Market(s)

Government and business organizations

Colors

Designer to choose colors to be used in the design.

Requirements
Must have
• Brochure Design
Nice to have
• Logos

```html
<!DOCTYPE html>
<html lang="en">
<head>
<meta charset="utf-8">
<title>Harbor Lantern Guidance – Brochure</title>
<link href="https://fonts.googleapis.com/css2?family=Archivo+Black&family=Open+Sans:ital,wght@0,400;0,600;0,700;1,400&display=swap" rel="stylesheet">
<style>
  :root{
    --navy:#1f2d3d;
    --navy-line:#c9d1da;
    --gold:#d9a22a;
    --gold-dark:#b9821a;
    --paper:#ffffff;
    --paper-shade:#eceef0;
    --ink:#1b1b1b;
    --stage:#e4ebf0;
    --water:#a9d3e3;
  }
  *{box-sizing:border-box;margin:0;padding:0}
  html,body{width:1134px;height:1200px;overflow:hidden}
  body{background:var(--stage);font-family:"Open Sans",Arial,sans-serif;color:var(--ink)}
  .sheet{position:absolute;left:17px;width:1100px;height:570px;display:flex;box-shadow:0 6px 18px rgba(0,0,0,.18)}
  .sheet--outside{top:20px}
  .sheet--inside{top:610px}
  .panel{width:366.66px;height:100%;display:flex;flex-direction:column;position:relative;overflow:hidden;background:var(--paper)}
  .panel + .panel{border-left:1px solid #d6d9dc}
  .panel-head{background:var(--navy);color:var(--gold);text-align:center;padding:16px 22px 14px;flex-shrink:0}
  .panel-title{font-family:"Archivo Black",Arial,sans-serif;font-size:19px;line-height:1.15;font-style:italic}
  .panel-sub{color:#fff;font-size:11px;font-weight:600;line-height:1.3;margin-top:8px}
  .panel-body{flex:1;min-height:0;padding:14px 28px;font-size:11.5px;line-height:1.45;background:linear-gradient(90deg,var(--paper) 85%,var(--paper-shade))}
  .panel-body p{margin-bottom:9px;text-align:center}
  .wave{display:block;width:100%;height:36px;flex-shrink:0}
  .panel-foot{background:var(--navy);display:flex;align-items:center;justify-content:center;flex-shrink:0}
  .art{display:block;flex-shrink:0}

  /* objectives */
  .objective-intro{text-align:center;margin-bottom:8px}
  .objective-head{font-family:"Archivo Black",Arial,sans-serif;font-size:10.5px;text-align:center;margin:6px 0 2px}
  .objective-list{list-style:none;font-size:10.5px;line-height:1.35;padding-left:6px}
  .objective-list span{color:#888;font-style:italic;margin-right:6px}

  /* programs */
  .panel--programs .panel-body{padding:10px 26px 8px;font-size:11px;line-height:1.4}
  .panel--programs .panel-body p{margin-bottom:4px}
  .program-head{font-family:"Archivo Black",Arial,sans-serif;font-size:10px;line-height:1.3;text-align:center;margin:4px 0 2px}
  .bullet-list{list-style:none;font-size:11.5px;line-height:1.3}
  .bullet-list li{padding-left:16px;position:relative}
  .bullet-list li::before{content:"";position:absolute;left:0;top:4px;width:8px;height:8px;border-radius:50%;background:#8a8a8a}
  .contacts{background:var(--gold);color:#fff;padding:10px 26px 12px;font-size:12px;line-height:1.4;flex-shrink:0}
  .contacts-title{font-weight:700;letter-spacing:.08em;margin-bottom:3px;display:flex;align-items:center;gap:8px}
  .contacts a{color:#fff;text-decoration:none;font-weight:700}

  /* cover */
  .panel--cover{background:var(--navy);color:#fff}
  .cover-frame{position:absolute;inset:18px;border:1px solid var(--navy-line)}
  .cover-name{position:absolute;top:150px;left:0;right:0;text-align:center;font-weight:700;font-size:34px;line-height:1.05;color:var(--gold)}
  .cover-mark{width:16px;height:16px;background:var(--gold);margin:0 auto 14px}
  .cover-tag{position:absolute;top:345px;left:50px;right:50px;border-top:1px solid var(--navy-line);border-bottom:1px solid var(--navy-line);padding:16px 0;text-align:center;font-size:15px;line-height:1.4}
  .cover-authors{position:absolute;bottom:38px;left:0;right:0;text-align:center;font-family:"Archivo Black",Arial,sans-serif;color:var(--gold);font-size:14px}

  /* inside */
  .inside-head{min-height:128px}
  .emph{font-weight:700;text-transform:uppercase}
</style>
</head>
<body>

<section class="sheet sheet--outside">
  <article class="panel panel--objectives">
    <header class="panel-head"><h2 class="panel-title">Harbor Lantern Guidance<br>(HLG) Objectives</h2></header>
    <div class="panel-body">
      <p class="objective-intro">HLG is about cultivating and capturing collective leadership resources in order to help chart a course through the dangers and opportunities of our time. Its objectives are as follows:</p>
      <h3 class="objective-head">IMPROVE ORGANIZATIONAL NAVIGATION</h3>
      <ul class="objective-list"><li><span>A</span>Avoid potential land mines</li><li><span>B</span>Exploit opportunities</li></ul>
      <h3 class="objective-head">INCREASE ACCOUNTABILITY</h3>
      <ul class="objective-list"><li><span>A</span>Constituency Accountability</li><li><span>B</span>Outcome Accountability</li><li><span>C</span>Process Accountability</li></ul>
      <h3 class="objective-head">ENHANCE COOPERATION</h3>
      <ul class="objective-list"><li><span>A</span>Create strong connections</li><li><span>B</span>Balance competition with cooperation</li><li><span>C</span>Incorporate strong, diverse individuals</li></ul>
    </div>
    <svg class="wave" viewBox="0 0 366 36" preserveAspectRatio="none"><rect width="366" height="36" fill="#1f2d3d"/><path d="M0 0H366V6Q183 40 0 6Z" fill="#fff"/><path d="M0 6Q183 40 366 6V14Q183 46 0 14Z" fill="#d9a22a"/></svg>
    <div class="panel-foot" style="height:150px">
      <svg class="art" role="img" aria-label="Illustration of three gold gears labelled skillful navigation, leadership influence and leadership influencers, linked by circular arrows" width="300" height="130"><rect width="300" height="130" rx="14" fill="#c7922a" opacity=".85"/></svg>
    </div>
  </article>

  <article class="panel panel--programs">
    <header class="panel-head"><h2 class="panel-title">HLG Programs</h2></header>
    <div class="panel-body">
      <p>HLG's comprehensive approach to improving leadership is transformational. However, it need not be implemented in its entirety to realize its benefits. It can be customized to meet the needs of small to large groups.</p>
      <h3 class="program-head">WHAT DOES IT INCLUDE?</h3>
      <ul class="bullet-list"><li>Day long or Half day workshops</li><li>Multi-Day workshops</li><li>Instruction and coaching</li></ul>
      <h3 class="program-head">WHAT ARE THE PROGRAMS ABOUT?</h3>
      <ul class="bullet-list"><li>Developing a CL Philosophy</li><li>Executing CL Processes</li><li>Growing CL Judgement</li><li>Leadership Roles for Everyone</li><li>Team Leadership</li><li>Building a CL Culture</li></ul>
      <h3 class="program-head">WHO COULD BENEFIT?</h3>
      <ul class="bullet-list"><li>Organizations</li><li>Professional Associations</li><li>Individuals, Teams and Small Groups</li></ul>
      <h3 class="program-head">HOW CAN IT HELP?</h3>
      <ul class="bullet-list"><li>Identify leadership strengths and weaknesses</li><li>Address Leadership trainings needs</li><li>Develop organizational leadership capacity</li></ul>
    </div>
    <footer class="contacts">
      <div class="contacts-title"><svg width="20" height="14" viewBox="0 0 20 14"><rect x="1" y="1" width="18" height="12" fill="none" stroke="#fff" stroke-width="1.5"/><path d="M1 1L10 8L19 1" fill="none" stroke="#fff" stroke-width="1.5"/></svg>CONTACTS</div>
      <div>Dale Harrow: <a>dale.harrow@example.com</a></div>
      <div>Tom Ardent: <a>t.ardent@example.net</a></div>
    </footer>
  </article>

  <article class="panel panel--cover">
    <div class="cover-frame"></div>
    <div class="cover-name"><div class="cover-mark"></div>Harbor<br>Lantern<br>Guidance</div>
    <p class="cover-tag">Identify and Engage the Collective Leadership in Your Organization</p>
    <p class="cover-authors">Dale Harrow &amp; Tom Ardent</p>
  </article>
</section>

<section class="sheet sheet--inside">
  <article class="panel panel--what">
    <header class="panel-head inside-head" style="min-height:112px">
      <h2 class="panel-title">What is Harbor Lantern Guidance?</h2>
      <p class="panel-sub">Leadership that cultivates and harvests collective human resources to help organizations navigate today's uncertain world</p>
    </header>
    <svg class="art" role="img" aria-label="Illustration of a diverse group of people representing collective leadership, set in a gold curved band" width="366" height="110" viewBox="0 0 366 110" preserveAspectRatio="none"><rect width="366" height="110" fill="#1f2d3d"/><path d="M0 0H366V40Q300 110 183 110Q66 110 0 40Z" fill="#d9a22a"/></svg>
    <div class="panel-body">
      <p>Identifying, growing, and channeling human resources is the primary role of Leadership.</p>
      <p>Skillful navigation, improved accountability, and enhanced levels of cooperation are magnified when collective knowledge, wisdom, and creativity are employed.</p>
      <p>Most leadership literature revolves around building individual capabilities. HLG is about tapping into the often-latent collective leadership resources in organizations.</p>
    </div>
  </article>

  <article class="panel panel--why">
    <header class="panel-head inside-head">
      <h2 class="panel-title">Why is Harbor Lantern Guidance important?</h2>
      <p class="panel-sub">Cooperative, accountable organizations that are on track are better prepared to respond to the unprecedented dangers and opportunities of today's world.</p>
    </header>
    <div class="panel-body">
      <p>It was sand that grounded the Meridian, the largest passenger ship afloat, on its maiden voyage.</p>
      <p>It was an owl (not the feathered kind) that guided the night convoys through the strait.</p>
      <p>What do these two events have in common? They both involve course corrections. One to avoid the "sand", and the other to heed the "owl".</p>
      <p>In a more amplified setting, today's organizations face sandbars of danger along with oceans of possibility. Without skillful navigation, an organization is either left adrift and missing opportunities, or is propelling toward unintended destinations with possible dire consequences.</p>
    </div>
    <svg class="wave" viewBox="0 0 366 36" preserveAspectRatio="none"><rect width="366" height="36" fill="#1f2d3d"/><path d="M0 0H366V4Q183 30 0 4Z" fill="#fff"/><path d="M0 4Q183 30 366 4V10Q183 36 0 10Z" fill="#d9a22a"/></svg>
    <div class="panel-foot" style="height:80px">
      <svg class="art" role="img" aria-label="Illustration representing the Owls and Sand metaphor" width="140" height="64"><rect width="140" height="64" rx="10" fill="#9ccbdc"/></svg>
    </div>
  </article>

  <article class="panel panel--how">
    <header class="panel-head inside-head">
      <h2 class="panel-title">How does Harbor Lantern Guidance work?</h2>
      <p class="panel-sub">By cultivating and deploying positive Collective Leadership Influence through constructive Collective Leadership Influencers.</p>
    </header>
    <div class="panel-body">
      <p>Like ripples through water, Leadership Influence penetrates an organization. Beneficial Leadership Influence has these characteristics; it must be positive, is both individual and collective, and both indirect and direct.</p>
      <p>Collective Leadership Influence begins with a <span class="emph">collective leadership philosophy</span>, grows through <span class="emph">collective leadership processes</span>, and matures with <span class="emph">collective leadership judgement</span>.</p>
      <p>Who bears responsibility for propelling Collective Leadership Influence? Influence cannot happen without competent Influencers. The three most important are: individuals, teams, and culture.</p>
    </div>
    <svg class="wave" viewBox="0 0 366 36" preserveAspectRatio="none"><rect width="366" height="36" fill="#1f2d3d"/><path d="M0 0H366V4Q183 30 0 4Z" fill="#fff"/><path d="M0 4Q183 30 366 4V10Q183 36 0 10Z" fill="#d9a22a"/></svg>
    <div class="panel-foot" style="height:80px">
      <svg class="art" role="img" aria-label="Illustration of a water drop making ripples" width="180" height="64"><ellipse cx="90" cy="34" rx="86" ry="28" fill="#a9d3e3"/></svg>
    </div>
  </article>
</section>

</body>
</html>
```